Website Layout for PlateNova

PlateNova is a company that will be dedicated (for now) to publishing recipes with the nutrition facts. Run by a nutritionist. In the future there may be a mobile app.

We need layout for 3 of the pages of the website. NO PROGRAMMING, only layout and graphic design. Not very complicated.

--Please view the details in the attached document--
We want a layout design for the pages: P.01, P.02 and P.03

Logo is also attached. Please don't hesitate if you want to modify the logo to fit your idea. The design should be clean, visually attractive and refreshing to look at. It should be sleek and a feel of technology, yet also natural and culinary.

Some examples to get ideas:

http://www.amberladlejournal.com/
http://www.tasliwavera.org/site/
http://thevelmorhaus.com/products/mix-slab
Updates

Project Deadline Extended
Reason: I extend the deadline for this week to allow you space for work on the observations made to your design and to provide the P.02 and P.03 designs. We greatly appreciate your hard work and are thrilled with your ideas.

Target Market(s)

Young people that live alone or want to optimize their cooking.
Young, modern housewives with a smartphone.

Industry/Entity Type

Nutrition

Requirements
Must have
• --Please view the details in the attached document--
NO PROGRAMMING. Only layout and graphic design.

```html
<!DOCTYPE html>
<html lang="en">
<head>
<meta charset="utf-8">
<title>PlateNova – Zucchini-Corn Casserole</title>
<link href="https://fonts.googleapis.com/css2?family=Open+Sans:wght@400;600&family=Roboto+Condensed:wght@400;700&display=swap" rel="stylesheet">
<style>
:root{
  --green:#4f9a2a;
  --green-light:#7cc242;
  --green-dark:#3f8a22;
  --red:#d9342b;
  --red-light:#ea5b3a;
  --orange:#e8951c;
  --text:#333;
  --muted:#555;
  --line:#cfcfcf;
  --panel-border:#d6d6d6;
  --footer-bg:#f5f5f5;
  --tab-grey:#dcdcdc;
  --khaki:#d6cb74;
}
*{box-sizing:border-box;margin:0;padding:0}
html,body{width:1138px;height:1200px;overflow:hidden;background:#fff}
body{font-family:"Open Sans",sans-serif;color:var(--text);font-size:14px}
.page{position:relative;width:1138px;height:1200px}
.abs{position:absolute}
.page-label{left:40px;top:5px;font-size:13px;color:#c8c8c8}
.social{left:41px;top:44px;display:flex;gap:7px}
.social span{width:24px;height:24px;border-radius:3px;display:block}
.social .s1{background:#e8951c}.social .s2{background:var(--red)}.social .s3{background:var(--green-light)}
.brand{left:440px;top:40px;display:flex;align-items:center;gap:12px}
.brand-mark{width:66px;height:66px;background:var(--green-light);border-radius:6px}
.brand-name{font-size:34px;font-weight:600;color:#3b3b3b;letter-spacing:-.5px}
.welcome{right:130px;top:43px;color:var(--red);font-size:15px;white-space:nowrap}
.logout{left:1018px;top:38px;width:80px;height:30px;background:var(--khaki);border:1px solid #c2b860;border-radius:2px;font-size:14px;color:#4a4a2a;display:flex;align-items:center;justify-content:center}
.search{left:306px;top:137px;width:524px;height:38px;border:1px solid #bdbdbd;border-radius:2px;display:flex}
.search input{flex:1;border:0;padding:0 12px;font:14px "Open Sans",sans-serif;color:#888;background:transparent}
.search button{width:40px;border:0;background:linear-gradient(var(--green-light),var(--green));display:flex;align-items:center;justify-content:center}
.crumbs{left:41px;top:199px;display:flex;align-items:center;gap:8px;font-size:13.5px}
.crumbs .sep{width:0;height:0;border-left:8px solid var(--red);border-top:5px solid transparent;border-bottom:5px solid transparent;margin:0 2px}
.crumbs .current{color:var(--green)}
.print{right:40px;top:201px;display:flex;align-items:center;gap:6px;font-size:13.5px}
.rule{left:36px;top:228px;width:1066px;height:1px;background:var(--line)}
.nutrition{left:41px;top:257px;width:257px;height:450px;border:1px solid var(--panel-border);border-radius:2px}
.nutrition h2{height:43px;background:linear-gradient(var(--green-light),var(--green));color:#fff;font:400 18px "Roboto Condensed",sans-serif;display:flex;align-items:center;gap:8px;padding-left:16px}
.nutrition .meta{padding:10px 13px 0;font-size:12.5px;line-height:19px}
.nutrition .head{display:flex;justify-content:space-between;margin:9px 10px 0 13px;padding-bottom:4px;border-bottom:3px solid #ccc;color:var(--red);font-size:14.5px}
.nutrition table{width:230px;margin-left:13px;border-collapse:collapse;font-size:14.5px}
.nutrition td{height:28.4px;border-bottom:1px solid #ccc;vertical-align:middle}
.nutrition tr:last-child td{border-bottom:0}
.nutrition td:last-child{width:70px}
.photo{background:radial-gradient(ellipse at 45% 40%,#f4efe6 0%,#c8a26a 35%,#b9552e 65%,#e9e4dc 100%)}
.hero{left:321px;top:257px;width:332px;height:271px;border:1px solid #ddd}
.arrow{width:49px;height:47px;background:linear-gradient(var(--green-light),var(--green));display:flex;align-items:center;justify-content:center}
.arrow.prev{left:306px;top:369px}.arrow.next{left:620px;top:369px}
.title{left:701px;top:271px;font:400 23px "Roboto Condensed",sans-serif;color:var(--green)}
.cats{left:701px;top:302px;font-size:15px}
.byline{left:701px;top:331px;font-size:13px}
.intro{left:701px;top:360px;width:400px;font-size:14.5px;line-height:21.5px;color:var(--muted)}
.ready{left:697px;top:462px;width:163px;height:42px;border:1px solid #ddd;display:flex;align-items:center;justify-content:center;font-size:14.5px}
.ready strong{color:var(--green);font-weight:600;font-size:18px;margin-left:5px}
.tab{top:547px;height:41px;display:flex;align-items:center;justify-content:center;font:400 18px "Roboto Condensed",sans-serif}
.tab.active{left:319px;width:156px;background:linear-gradient(var(--green-light),var(--green));color:#fff}
.tab.idle{left:481px;width:154px;background:linear-gradient(#eee,var(--tab-grey));color:#444}
.ingredients{left:320px;top:588px;width:778px;height:331px;border:1px solid #ddd}
.servings{position:absolute;left:24px;top:20px;font-size:14.5px}
.ingredients ul{position:absolute;left:24px;top:52px;list-style:none;font-size:14.5px;color:#444}
.ingredients li{height:24.8px;display:flex;align-items:center;gap:8px}
.ingredients li::before{content:"";border-left:8px solid var(--red);border-top:5px solid transparent;border-bottom:5px solid transparent}
.side-photo{left:521px;top:42px;width:224px;height:260px}
.btn{top:934px;height:40px;display:flex;align-items:center;gap:8px;padding:0 12px;color:#fff;font-size:14.5px;font-weight:600;white-space:nowrap}
.btn.create{left:319px;width:191px;background:linear-gradient(90deg,var(--red),var(--red-light))}
.btn.edit{left:520px;width:128px;background:var(--orange)}
.footer-nav{left:0;top:1034px;width:1138px;display:flex;justify-content:center;font:400 18px "Roboto Condensed",sans-serif}
.footer-nav a{display:flex;align-items:center;gap:8px;padding:0 12px;height:34px;color:#222;text-decoration:none}
.footer-nav a+a{border-left:1px solid #ccc}
.footer{left:0;top:1090px;width:1138px;height:110px;background:var(--footer-bg);border-top:1px solid #e4e4e4}
.footer .mark{position:absolute;left:44px;top:20px;width:70px;height:70px;background:var(--green-light);border-radius:6px}
.footer .copy{position:absolute;left:130px;top:48px;font-size:14px;color:#555}
.footer .contact{position:absolute;right:40px;top:36px;text-align:right;font-size:14px;line-height:22px;color:#222}
</style>
</head>
<body>
<div class="page">
  <div class="abs page-label">Recipe Page Mockup 1</div>
  <div class="abs social" aria-label="Social links"><span class="s1"></span><span class="s2"></span><span class="s3"></span></div>
  <div class="abs brand"><span class="brand-mark"></span><span class="brand-name">PlateNova</span></div>
  <div class="abs welcome">Welcome Marisol Keane</div>
  <div class="abs logout">Log out</div>

  <div class="abs search">
    <input type="text" value="Enter Your Searh Items" aria-label="Search">
    <button aria-label="Search"><svg width="20" height="20" viewBox="0 0 20 20"><circle cx="8" cy="8" r="5.5" fill="none" stroke="#fff" stroke-width="2.5"/><line x1="12" y1="12" x2="17" y2="17" stroke="#fff" stroke-width="3" stroke-linecap="round"/></svg></button>
  </div>

  <nav class="abs crumbs"><span>Home</span><i class="sep"></i><span>Category One</span><i class="sep"></i><span>Recipe List</span><i class="sep"></i><span class="current">Zucchini-Corn Casserole</span></nav>
  <div class="abs print"><svg width="19" height="17" viewBox="0 0 19 17"><rect x="4" y="0" width="11" height="5" fill="var(--red)"/><rect x="0" y="5" width="19" height="8" rx="2" fill="var(--red)"/><rect x="4" y="10" width="11" height="7" fill="#fff" stroke="var(--red)" stroke-width="1.5"/></svg>Print Recipe</div>
  <div class="abs rule"></div>

  <aside class="abs nutrition">
    <h2><svg width="30" height="22" viewBox="0 0 30 22"><path d="M4 18a11 11 0 0 1 22 0z" fill="#fff6c8"/><rect x="1" y="18" width="28" height="3" rx="1" fill="#fff6c8"/><circle cx="15" cy="6" r="1.6" fill="#fff6c8"/></svg>NUTRITIONAL FACTS</h2>
    <div class="meta">Serving Size: 1 (234 g)<br>Servings Per Recipe: 8</div>
    <div class="head"><span>Amount Per Serving</span><span>% Daily Value</span></div>
    <table>
      <tr><td>Calories</td><td>700 kcal</td></tr>
      <tr><td>Fat</td><td>95 g</td></tr>
      <tr><td>Carbohydrates</td><td>75 g</td></tr>
      <tr><td>Protein</td><td>90 g</td></tr>
      <tr><td>Cholesterol</td><td>77 mg</td></tr>
      <tr><td>Vitamin A</td><td>400 µg</td></tr>
      <tr><td>Vitamin B</td><td>200 mg</td></tr>
      <tr><td>Vitamin C</td><td>40 mg</td></tr>
      <tr><td>Calcium</td><td>100 mg</td></tr>
      <tr><td>Iron</td><td>32 mg</td></tr>
      <tr><td>Sodium</td><td>15 g</td></tr>
    </table>
  </aside>

  <div class="abs hero photo" role="img" aria-label="Photo of plated casserole dishes on a festive table"></div>
  <div class="abs arrow prev"><svg width="16" height="24" viewBox="0 0 16 24"><polyline points="13,2 3,12 13,22" fill="none" stroke="#fff" stroke-width="2.5"/></svg></div>
  <div class="abs arrow next"><svg width="16" height="24" viewBox="0 0 16 24"><polyline points="3,2 13,12 3,22" fill="none" stroke="#fff" stroke-width="2.5"/></svg></div>

  <h1 class="abs title">ZUCCHINI-CORN CASSEROLE</h1>
  <div class="abs cats"><b style="font-weight:600">Categories:</b> Corn, Peppers, Eggs/dairy</div>
  <div class="abs byline">Recipe by Marisol Keane</div>
  <p class="abs intro">Lorem ipsum dolor sit amet, consectetur adipiscing elit. Ut sit amet metus ut lorem pharetra venenatis fermentum at nibh. Nulla aliquet diam eu turpis convallis sit amet male-suada mi ultrices. In in velit massa, vitae condimentum leo.</p>
  <div class="abs ready">Ready in <strong>40 mins</strong></div>

  <div class="abs tab active">INGREDIENTS</div>
  <div class="abs tab idle">DIRECTIONS</div>
  <section class="abs ingredients">
    <div class="servings"><b style="font-weight:600">Servings:</b> 8-10 Peoples</div>
    <ul>
      <li>3 lbs small zucchini, trimmed and scrubbed</li>
      <li>1 (1 lb) can cream-style corn</li>
      <li>4 eggs, beaten</li>
      <li>2 tablespoons butter or 2 tablespoons margarine</li>
      <li>1 medium onion, chopped</li>
      <li>1 small green pepper, chopped</li>
      <li>1/4 teaspoon salt</li>
      <li>1/4 teaspoon pepper</li>
      <li>1 cup shredded cheddar cheese (4 ounces)</li>
      <li>paprika</li>
    </ul>
    <div class="abs side-photo photo" role="img" aria-label="Photo of the finished casserole served on plates"></div>
  </section>

  <div class="abs btn create"><svg width="26" height="20" viewBox="0 0 30 22"><path d="M4 18a11 11 0 0 1 22 0z" fill="#fff"/><rect x="1" y="18" width="28" height="3" rx="1" fill="#fff"/></svg>Create New Recipe</div>
  <div class="abs btn edit"><svg width="22" height="20" viewBox="0 0 22 20"><rect x="1" y="3" width="15" height="15" rx="2" fill="none" stroke="#fff" stroke-width="2"/><path d="M8 12l10-10 3 3-10 10H8z" fill="#fff"/></svg>Edit Recipe</div>

  <nav class="abs footer-nav">
    <a href="#"><svg width="18" height="17" viewBox="0 0 18 17"><path d="M9 1L1 8h2v8h4v-5h4v5h4V8h2z" fill="var(--green)"/></svg>Home</a>
    <a href="#"><svg width="14" height="18" viewBox="0 0 14 18"><rect x="1" y="1" width="12" height="16" rx="1" fill="var(--red)"/><rect x="3" y="4" width="8" height="2" fill="#fff"/></svg>About</a>
    <a href="#"><svg width="26" height="18" viewBox="0 0 26 18"><circle cx="8" cy="6" r="4" fill="var(--orange)"/><path d="M1 17a7 6 0 0 1 14 0z" fill="var(--orange)"/><circle cx="18" cy="6" r="4" fill="#d06a1a"/><path d="M11 17a7 6 0 0 1 14 0z" fill="#d06a1a"/></svg>Contact Us</a>
  </nav>

  <footer class="abs footer">
    <span class="mark"></span>
    <div class="copy">© 2014 by PlateNova. All Rights Reserved</div>
    <div class="contact">info@platenova.com<br>+1 555 204 31870</div>
  </footer>
</div>
</body>
</html>
```